Modify mobile web Photoshop design to make them look great

We need to choose and refine the stock image to look great on 5 mobile web pages: 1) Hourglass image on home screen, 2) Sofa image on registration screen, 3) Loveseat image on login screen, 4) Lamp for reminder screen, and 5) Bed for ratings / score screen. Sample photos denote what customer wants, but they are just downloaded from Brindo, and is not purchased stock photos. Designers need to show that the updated photos used are properly purchased from stock photo source. Photoshop files for all 5 mobile web pages are provided. Artists are requested to edit and submit the 5 photoshop files and make them look as good as possible with the constraints above. No change is needed on the layout or anything beside the 5 stock images, but subtle refinements are OK if you believe it would improve the overall design without affecting the art direction.

Target Market(s)

Travel, Lifestyle

Industry/Entity Type

Hospitality

Font styles to use
Sans Serif

Requirements
Must have
• Stock photos must be properly licensed, artists must put updated stock photos back into supplied photoshop source files, updated look and feel should have the same general art direction, images must be hourglass, sofa, loveseat, lamp and bed
Nice to have
• Minor and very subtle touchup of other elements without affecting any design work of the layout such as color scheme
Should not have
• Should not affect art direction, identity and color of all design and layout elements, should not use stock image other than the types specified (hourglass, sofa, loveseat, lamp and bed), should not use images not licensed from stock photo sites

```html
<!DOCTYPE html>
<html lang="en">
<head>
<meta charset="utf-8">
<title>Lounara – Register</title>
<link href="https://fonts.googleapis.com/css2?family=Source+Sans+3:wght@400;600;800&display=swap" rel="stylesheet">
<style>
  :root {
    --bg: #e8e3df;
    --ink: #111111;
    --field-text: #555555;
    --purple: #b07fd8;
    --teal: #0f9692;
    --magenta: #a0157a;
    --peach: #f2b382;
    --white: #ffffff;
    --divider: #9a9a9a;
    --photo-top: #d5d2cf;
    --photo-mid: #c4bfbd;
    --photo-low: #b8b3b2;
  }
  * { box-sizing: border-box; margin: 0; padding: 0; }
  html, body { width: 676px; height: 1200px; overflow: hidden; }
  body {
    background: var(--bg);
    font-family: "Source Sans 3", sans-serif;
    position: relative;
  }
  .hero-photo {
    position: absolute; left: 0; top: 0; width: 676px; height: 915px;
    background: linear-gradient(180deg,
      var(--photo-top) 0%,
      var(--photo-top) 38%,
      var(--photo-mid) 55%,
      var(--photo-low) 72%,
      var(--photo-mid) 86%,
      var(--bg) 100%);
  }
  .site-header {
    position: absolute; left: 0; top: 0; width: 676px; height: 95px;
  }
  .back-link { position: absolute; left: 36px; top: 28px; }
  .brand-name {
    position: absolute; left: 0; right: 0; top: 12px; text-align: center;
    font-weight: 800; font-size: 50px; letter-spacing: -1px; line-height: 1.2; color: var(--ink);
  }
  .menu-toggle { position: absolute; left: 602px; top: 38px; }
  .register-panel {
    position: absolute; left: 27px; top: 344px; width: 620px; height: 558px;
    border: 1.5px solid rgba(255,255,255,0.9); border-radius: 9px;
  }
  .field {
    position: absolute; left: 54px; width: 508px; height: 48px;
    background: var(--white); display: flex; align-items: center;
    border-bottom: 1.5px solid var(--line);
  }
  .field-icon {
    width: 56px; height: 32px; flex: none;
    display: flex; align-items: center; justify-content: center;
    border-right: 1px solid var(--divider);
  }
  .field-label { padding-left: 12px; font-size: 19px; line-height: 1; color: var(--field-text); flex: 1; white-space: nowrap; }
  .dob-tag { font-size: 15px; color: var(--magenta); }
  .calendar { margin-right: 14px; flex: none; }
  .register-button {
    position: absolute; left: 55px; top: 475px; width: 506px; height: 47px;
    background: var(--peach); border-radius: 4px; border: none;
    color: var(--white); font-family: inherit; font-size: 22px; text-transform: uppercase;
    display: flex; align-items: center; justify-content: center;
  }
  .pager {
    position: absolute; top: 1091px; left: 267px; display: flex; gap: 13px;
  }
  .pager span { width: 20px; height: 20px; border-radius: 50%; }
</style>
</head>
<body>
  <div class="hero-photo" role="img" aria-label="Photo placeholder: sofa with red cushions against a grey concrete wall"></div>

  <header class="site-header">
    <svg class="back-link" width="24" height="34" viewBox="0 0 24 34"><path d="M19 3 L5 17 L19 31" fill="none" stroke="#111" stroke-width="4"/></svg>
    <div class="brand-name">Lounara</div>
    <svg class="menu-toggle" width="34" height="18" viewBox="0 0 34 18"><g stroke="#111" stroke-width="2"><line x1="0" y1="1" x2="34" y2="1"/><line x1="0" y1="8" x2="34" y2="8"/><line x1="0" y1="15" x2="34" y2="15"/></g></svg>
  </header>

  <form class="register-panel">
    <div class="field" style="top:46px; --line: var(--purple);">
      <div class="field-icon"><svg width="24" height="28" viewBox="0 0 24 28" fill="none" stroke="#b07fd8" stroke-width="1.5"><circle cx="12" cy="8" r="6"/><path d="M2 26 C2 17 22 17 22 26 Z"/></svg></div>
      <span class="field-label">Full Name</span>
    </div>
    <div class="field" style="top:117px; --line: #444;">
      <div class="field-icon"><svg width="32" height="22" viewBox="0 0 32 22" fill="none" stroke="#0f9692" stroke-width="1.6"><rect x="1" y="1" width="30" height="20" rx="2"/><rect x="4" y="4" width="11" height="14"/><circle cx="9.5" cy="9" r="2.5"/><path d="M5 17 C6 12 13 12 14 17"/><line x1="18" y1="8" x2="28" y2="8"/><line x1="18" y1="12" x2="28" y2="12"/></svg></div>
      <span class="field-label">&nbsp;ID Number</span>
    </div>
    <div class="field" style="top:188px; --line: var(--magenta);">
      <div class="field-icon"><span class="dob-tag">DOB</span></div>
      <span class="field-label">&nbsp;06/09/1980</span>
      <svg class="calendar" width="26" height="28" viewBox="0 0 26 28"><rect x="1" y="4" width="24" height="23" rx="3" fill="#a0157a"/><rect x="4" y="11" width="18" height="13" fill="#fff"/><rect x="6" y="0" width="3" height="7" fill="#a0157a"/><rect x="17" y="0" width="3" height="7" fill="#a0157a"/><g fill="#a0157a"><rect x="6" y="13" width="3" height="3"/><rect x="11.5" y="13" width="3" height="3"/><rect x="17" y="13" width="3" height="3"/><rect x="6" y="19" width="3" height="3"/><rect x="11.5" y="19" width="3" height="3"/><rect x="17" y="19" width="3" height="3"/></g></svg>
    </div>
    <div class="field" style="top:258px; --line: var(--peach);">
      <div class="field-icon"><svg width="20" height="32" viewBox="0 0 20 32" fill="none" stroke="#f2b382" stroke-width="1.8"><rect x="2" y="1" width="16" height="30" rx="2"/><line x1="2" y1="6" x2="18" y2="6"/><line x1="2" y1="25" x2="18" y2="25"/></svg></div>
      <span class="field-label">Mobile Number</span>
    </div>
    <div class="field" style="top:329px; --line: #444;">
      <div class="field-icon"><svg width="26" height="26" viewBox="0 0 26 26"><circle cx="17" cy="9" r="7" fill="#0f9692"/><circle cx="19" cy="7" r="2" fill="#fff"/><path d="M12 13 L3 22 L3 25 L7 25 L7 22 L10 22 L10 19 L13 19 L15 16 Z" fill="#0f9692"/></svg></div>
      <span class="field-label">Set Password</span>
    </div>
    <div class="field" style="top:400px; --line: var(--purple);">
      <div class="field-icon"><svg width="24" height="16" viewBox="0 0 24 16"><rect x="0" y="0" width="24" height="16" fill="#b07fd8"/><path d="M0 0 L12 9 L24 0" fill="none" stroke="#fff" stroke-width="1.5"/><path d="M0 16 L9 7 M24 16 L15 7" stroke="#fff" stroke-width="1"/></svg></div>
      <span class="field-label">Email</span>
    </div>
    <button class="register-button" type="submit">Register Now</button>
  </form>

  <nav class="pager" aria-label="Pages">
    <span style="background: var(--purple);"></span>
    <span style="background: var(--teal);"></span>
    <span style="background: var(--magenta);"></span>
    <span style="background: var(--peach);"></span>
    <span style="background: var(--teal);"></span>
  </nav>
</body>
</html>
```